New business card design

I need original, modern, business looking but dzen (minimalistic) looking design.
Also refer to websit qvtrenda.ru

Text is

Зорин Виктор, PMP
Партнер

Моб. +7 (915) 460 1897
info@qvtrenda.ru
Москва, Россия, 117358, ул. Берёзовая 27/2
=====================

Zorin Viktor, PMP
Partner

Mob. +7 (915) 460 1897
info@qvtrenda.ru
Moscow, Russia,117358, Beryozovaya 27/2

```html
<!DOCTYPE html>
<html lang="ru">
<head>
<meta charset="utf-8">
<title>QVTrenda — визитная карточка</title>
<link rel="stylesheet" href="https://fonts.googleapis.com/css2?family=Arimo:wght@400&display=swap">
<style>
  :root {
    --backdrop: #1f2021;
    --card-dark: #2c2e2f;
    --card-light: #ffffff;
    --brand-cyan: #2cb8d6;
    --brand-blue: #1a86c8;
    --brand-faint: #d3e8f7;
    --ink: #1c1c1c;
    --ink-soft: #333333;
    --on-dark: #f2f2f2;
  }
  * { margin: 0; padding: 0; box-sizing: border-box; }
  html, body {
    width: 1200px;
    height: 900px;
    overflow: hidden;
    background: var(--backdrop);
    font-family: "Arimo", Arial, sans-serif;
  }
  .canvas {
    position: relative;
    width: 1200px;
    height: 900px;
  }
  .card {
    position: absolute;
    width: 630px;
    height: 350px;
    overflow: hidden;
  }
  .card--back {
    left: 70px;
    top: 70px;
    background: var(--card-dark);
  }
  .card--front {
    left: 500px;
    top: 480px;
    background: var(--card-light);
  }
  .brand {
    position: absolute;
    display: flex;
    align-items: center;
    gap: 22px;
  }
  .brand__mark {
    width: 86px;
    height: 86px;
    background: var(--brand-blue);
    border-radius: 10px;
  }
  .brand__name {
    font-size: 70px;
    font-weight: 400;
    letter-spacing: -1px;
    line-height: 1;
  }
  .card--back .brand { left: 100px; top: 132px; }
  .card--back .brand__name { color: var(--on-dark); }
  .card--front .brand { left: 70px; top: 50px; }
  .card--front .brand__name { color: var(--brand-cyan); }
  .faint-mark {
    position: absolute;
    right: -40px;
    top: 40px;
    width: 150px;
    height: 150px;
    background: var(--brand-faint);
    border-radius: 14px;
  }
  .contact {
    position: absolute;
    left: 70px;
    top: 180px;
    color: var(--ink-soft);
  }
  .contact__name {
    font-size: 22px;
    color: var(--ink);
  }
  .contact__cert { font-size: 15px; }
  .contact__role {
    font-size: 15px;
    color: var(--brand-cyan);
    margin-top: 2px;
  }
  .contact__list {
    list-style: none;
    margin-top: 12px;
    font-size: 16px;
    line-height: 21px;
  }
  .contact__list li {
    display: flex;
    align-items: center;
    gap: 10px;
  }
  .contact__icon {
    width: 14px;
    height: 14px;
    flex: none;
  }
  .contact__address {
    margin-top: 12px;
    font-size: 16px;
    line-height: 21px;
  }
</style>
</head>
<body>
<main class="canvas">

  <section class="card card--back" aria-label="Оборотная сторона визитки">
    <div class="brand">
      <span class="brand__mark"></span>
      <span class="brand__name">QVTrenda</span>
    </div>
  </section>

  <section class="card card--front" aria-label="Лицевая сторона визитки">
    <span class="faint-mark"></span>
    <div class="brand">
      <span class="brand__mark"></span>
      <span class="brand__name">QVTrenda</span>
    </div>

    <div class="contact">
      <p class="contact__name">Зорин Виктор, <span class="contact__cert">PMP</span></p>
      <p class="contact__role">Партнер</p>
      <ul class="contact__list">
        <li>
          <svg class="contact__icon" viewBox="0 0 14 14" aria-hidden="true">
            <rect x="3.5" y="1" width="7" height="12" rx="1.3" fill="none" stroke="#2cb8d6" stroke-width="1.5"/>
            <rect x="5.5" y="10.3" width="3" height="1.2" fill="#2cb8d6"/>
          </svg>
          +7 (915) 460 1897
        </li>
        <li>
          <svg class="contact__icon" viewBox="0 0 14 14" aria-hidden="true">
            <rect x="1" y="3" width="12" height="8.5" fill="#2cb8d6"/>
            <path d="M1 3 L7 8 L13 3" fill="none" stroke="#ffffff" stroke-width="1.2"/>
          </svg>
          info@qvtrenda.ru
        </li>
      </ul>
      <p class="contact__address">Москва, Россия, 117358, ул.<br>Берёзовая 27/2</p>
    </div>
  </section>

</main>
</body>
</html>
```